Facebook & Instagram Ad Design for Chiropractor

I'd like a series of ads developed for our chiropractic office to use on Facebook and Instagram. I've attached the versions we're using today. They need to be updated. The offer content would be generally the same. There are two types of ads we're seeking. One for basic chiropractic services and the other for chiropractic decompression services.

Current ads can be seen in attached and here:
https://lnk.example/8TrQ2zXvPoLkm3A

Learn more about the company at www.bellwingchiropractic.example

Target Market(s)

Potential patients seeking chiropractic care or who are unaware that chiropractic could help them (suffer from back pain, etc.) in the greater Green Bay, WI area.

Industry/Entity Type

Chiropractic

Font styles to use
Sans Serif

Colors
0592cd
3277b5

Requirements
Must have
• Compelling visuals
Comply with text requirements for FB & Insta ads
Should not have
• Clinical images that depict traditional medical care

```html
<!DOCTYPE html>
<html lang="en">
<head>
<meta charset="utf-8">
<title>New Patient Offer – Bellwing Chiropractic</title>
<link rel="stylesheet" href="https://fonts.googleapis.com/css2?family=Montserrat:ital,wght@0,300;1,900&family=Roboto+Condensed:wght@700&family=Open+Sans:wght@400&display=swap">
<style>
  :root {
    --navy-deep: #06314f;
    --navy: #0c5283;
    --brand-blue: #3277b5;
    --sky-blue: #0592cd;
    --white: #ffffff;
    --ink: #14263d;
    --ink-soft: #222222;
    --photo-haze: #b9b6b2;
    --photo-charcoal: #2c2f34;
    --photo-slate: #44474c;
    --photo-skin-deep: #b88b72;
    --photo-skin: #dcbba6;
    --photo-light: #efe9e4;
  }
  * { margin: 0; padding: 0; box-sizing: border-box; }
  html, body { width: 1200px; height: 627px; overflow: hidden; background: var(--white); }
  .ad {
    position: relative;
    width: 1200px;
    height: 627px;
    overflow: hidden;
    background: var(--white);
  }
  .hero-photo {
    position: absolute;
    left: 0; top: 0;
    width: 1200px; height: 565px;
    background: linear-gradient(100deg,
      var(--photo-haze) 0%,
      var(--photo-slate) 22%,
      var(--photo-charcoal) 42%,
      var(--photo-charcoal) 54%,
      var(--photo-skin-deep) 66%,
      var(--photo-skin) 80%,
      var(--photo-light) 100%);
  }
  .wave {
    position: absolute;
    left: 0; top: 0;
    width: 1200px; height: 565px;
  }
  .headline {
    position: absolute;
    left: 46px;
    top: 44px;
    color: var(--white);
    font-family: "Montserrat", sans-serif;
    font-weight: 900;
    font-style: italic;
    font-size: 104px;
    line-height: 100px;
    letter-spacing: -1px;
    text-transform: uppercase;
  }
  .offer {
    position: absolute;
    left: 50px;
    top: 296px;
    color: var(--white);
    font-family: "Montserrat", sans-serif;
    font-weight: 300;
    font-size: 44px;
    letter-spacing: 1px;
    text-transform: uppercase;
  }
  .footer {
    position: absolute;
    left: 0; top: 565px;
    width: 1200px; height: 62px;
    background: var(--white);
    display: flex;
    align-items: center;
    justify-content: space-between;
    padding: 0 30px 0 22px;
  }
  .brand-name {
    font-family: "Roboto Condensed", sans-serif;
    font-weight: 700;
    font-size: 24px;
    color: var(--ink);
  }
  .site-url {
    font-family: "Open Sans", sans-serif;
    font-weight: 400;
    font-size: 12px;
    color: var(--ink-soft);
  }
</style>
</head>
<body>
  <main class="ad">
    <div class="hero-photo" role="img" aria-label="Close-up of a chiropractor's hands pressing on a patient's lower back during a treatment"></div>

    <svg class="wave" viewBox="0 0 1200 565" aria-hidden="true">
      <defs>
        <linearGradient id="navyFill" x1="0" y1="0" x2="1" y2="0">
          <stop offset="0" stop-color="var(--navy-deep)"/>
          <stop offset="1" stop-color="var(--navy)"/>
        </linearGradient>
        <linearGradient id="skyFill" x1="0" y1="0" x2="1" y2="1">
          <stop offset="0" stop-color="var(--brand-blue)"/>
          <stop offset="1" stop-color="var(--sky-blue)"/>
        </linearGradient>
      </defs>
      <path d="M0,0 H820 C700,40 630,75 600,150 C565,250 535,380 385,420 C255,455 120,450 0,462 Z" fill="url(#skyFill)"/>
      <path d="M0,0 H555 C505,55 535,150 525,240 C510,340 435,388 315,398 C195,408 90,418 0,436 Z" fill="url(#navyFill)"/>
    </svg>

    <h1 class="headline">New<br>Patient</h1>
    <p class="offer">Offer $25</p>

    <footer class="footer">
      <span class="brand-name">Bellwing Chiropractic</span>
      <span class="site-url">www.baytown-spinecare.example</span>
    </footer>
  </main>
</body>
</html>
```